We need visit card and a letter paper for our website. thx

We have a beauty clinic in Switzerland.
https://wiesentalblick.ch
We need a visit card.

Requirements
Must have
• see colors on website

```html
<!DOCTYPE html>
<html lang="de">
<head>
<meta charset="utf-8">
<title>Wiesentalblick – Visitenkarte</title>
<link href="https://fonts.googleapis.com/css2?family=Josefin+Sans:wght@300&family=Arimo:wght@400&display=swap" rel="stylesheet">
<style>
  :root {
    --page-bg: #efefef;
    --card-white: #fbfbfa;
    --ink: #1a1a1a;
    --ink-soft: #2e2e2e;
    --rose-light: #e6c7c4;
    --rose-mid: #c99d9b;
    --rose-deep: #a87877;
    --berry: #9c2a4e;
    --white: #ffffff;
  }
  * { margin: 0; padding: 0; box-sizing: border-box; }
  html, body {
    width: 1200px;
    height: 892px;
    overflow: hidden;
    background: var(--page-bg);
  }
  .sheet {
    position: relative;
    width: 1200px;
    height: 892px;
    display: flex;
    align-items: center;
    justify-content: center;
    gap: 48px;
  }
  .card {
    position: relative;
    width: 520px;
    height: 336px;
    overflow: hidden;
    box-shadow: 0 10px 26px rgba(0,0,0,0.12);
  }
  .card--front { background: var(--card-white); }
  .card--back { background: var(--rose-mid); }

  .wordmark {
    position: absolute;
    display: flex;
    align-items: center;
    gap: 12px;
    font-family: "Josefin Sans", sans-serif;
    font-weight: 300;
    font-size: 40px;
    letter-spacing: 0.5px;
    line-height: 1;
  }
  .wordmark__square {
    width: 12px;
    height: 12px;
  }
  .card--front .wordmark {
    top: 62px;
    right: 44px;
    color: var(--ink);
  }
  .card--front .wordmark__square { background: var(--ink); }

  .contact {
    position: absolute;
    left: 44px;
    bottom: 42px;
    font-family: "Arimo", sans-serif;
    color: var(--ink-soft);
  }
  .contact__name {
    font-size: 22px;
    color: var(--ink);
    margin-bottom: 3px;
  }
  .contact__role {
    font-size: 14px;
    margin-bottom: 20px;
  }
  .contact__line {
    font-size: 13px;
    line-height: 1.55;
  }

  .card__photo {
    position: absolute;
    inset: 0;
    background: linear-gradient(135deg, var(--rose-light) 0%, var(--rose-mid) 55%, var(--rose-deep) 100%);
  }
  .card--back .wordmark {
    top: 50%;
    left: 50%;
    transform: translate(-50%, -50%);
    color: var(--white);
  }
  .card--back .wordmark__square { background: var(--berry); }
</style>
</head>
<body>
<main class="sheet">
  <section class="card card--front" aria-label="Visitenkarte Vorderseite">
    <div class="wordmark">
      <span class="wordmark__square"></span>
      <span class="wordmark__name">Wiesentalblick</span>
    </div>
    <div class="contact">
      <p class="contact__name">Dr. Lea Moser</p>
      <p class="contact__role">Plastische Chirurgie</p>
      <p class="contact__line">+41 (0) 800 24 60 80</p>
      <p class="contact__line">hallo@wiesentalblick.ch</p>
      <p class="contact__line">Lindenweg 14, 7412 Talheim, Schweiz</p>
    </div>
  </section>

  <section class="card card--back" aria-label="Visitenkarte Rückseite">
    <div class="card__photo" role="img" aria-label="Foto: Frau in dunkler Wäsche liegt entspannt auf hellrosa Bettlaken, rosé getönt"></div>
    <div class="wordmark">
      <span class="wordmark__square"></span>
      <span class="wordmark__name">Wiesentalblick</span>
    </div>
  </section>
</main>
</body>
</html>
```